Heal the world with your creativity.

We're looking for advertising materials (social media, email, etc) for a new mental health platform called PIVOT (www.viewpivot.tv). PIVOT’s mission is to empower our members to heal and thrive by making expert advice and real-life experiences accessible to all.

Note

Facebook Cover Images: 820 x 312 pixels
LinkedIn Cover Images: 1128 x 191 pixels
3 x Social Media Post Image Templates: 1080 x 1080 pixles
3 x Enewsletter Header Image Templates: 1080 x 360 pixels
Sales One sheet: US Letter (8.5 x 11 inches)
Overview Powerpoint template: 13.33 x 7.5 inches

Fonts to Use:
Galanogrotesque
Montserrat regular

Target Market(s)

18 - 35 year olds

Industry/Entity Type

Mental Health

Requirements
Must have
• Facebook Cover Images: 820 x 312 pixels
3 x Enewsletter Header Images: 1080 x 360 pixels

Fonts to Use:
Galanogrotesque
Montserrat regular
Nice to have
• Creative copywriting for social media posts

```html
<!DOCTYPE html>
<html lang="en">
<head>
<meta charset="utf-8">
<title>PIVOT – Your Mental Health Made Simple</title>
<link rel="stylesheet" href="https://fonts.googleapis.com/css2?family=Anton&family=Lato:wght@700&family=Outfit:wght@600;700&display=swap">
<style>
  :root {
    --orange: #f7860f;
    --navy: #2b4a62;
    --ink: #1f2a33;
    --sky-light: #8bcdf1;
    --sky: #4aaee3;
    --white: #ffffff;
    --photo-light: #eef2f4;
    --photo-mid: #c9d1d6;
    --photo-dark: #8e979c;
    --leaf: #258a7c;
    --head: #2a4b63;
  }
  * { margin: 0; padding: 0; box-sizing: border-box; }
  html, body { width: 1200px; height: 401px; overflow: hidden; background: var(--white); }
  .banner {
    position: relative;
    width: 1200px;
    height: 401px;
    overflow: hidden;
    background: var(--white);
  }
  .layer { position: absolute; inset: 0; width: 1200px; height: 401px; }
  .brand {
    position: absolute;
    left: 402px;
    top: 160px;
    display: flex;
    align-items: center;
    gap: 7px;
  }
  .brand-dot {
    width: 12px;
    height: 12px;
    border-radius: 50%;
    background: var(--orange);
  }
  .brand-name {
    font-family: "Outfit", sans-serif;
    font-weight: 700;
    font-size: 24px;
    line-height: 1;
    color: var(--navy);
    letter-spacing: 1px;
  }
  .headline {
    position: absolute;
    left: 500px;
    top: 84px;
  }
  .headline-lead {
    display: block;
    font-family: "Outfit", sans-serif;
    font-weight: 600;
    font-size: 43px;
    line-height: 1;
    color: var(--orange);
    letter-spacing: -0.3px;
    white-space: nowrap;
  }
  .headline-main {
    display: block;
    font-family: "Anton", sans-serif;
    font-weight: 400;
    font-size: 70px;
    line-height: 1;
    color: var(--navy);
    margin-top: 2px;
    margin-left: 6px;
    letter-spacing: 0.5px;
    white-space: nowrap;
  }
  .intro {
    position: absolute;
    left: 507px;
    top: 208px;
    width: 370px;
    font-family: "Lato", sans-serif;
    font-weight: 700;
    font-size: 17.8px;
    line-height: 22px;
    color: var(--ink);
  }
</style>
</head>
<body>
  <div class="banner">
    <svg class="layer" viewBox="0 0 1200 401" role="img" aria-label="Photo of a young woman sitting on a chair by a bright window, hugging her knees">
      <defs>
        <linearGradient id="photoTone" x1="0" y1="0" x2="1" y2="1">
          <stop offset="0" stop-color="var(--photo-light)"/>
          <stop offset="0.6" stop-color="var(--photo-mid)"/>
          <stop offset="1" stop-color="var(--photo-dark)"/>
        </linearGradient>
      </defs>
      <path d="M0,0 L352,0 C385,35 395,95 388,150 C382,210 392,280 432,335 L432,401 L0,401 Z" fill="url(#photoTone)"/>
    </svg>

    <svg class="layer" viewBox="0 0 1200 401" aria-hidden="true">
      <path d="M352,0 C385,35 395,95 388,150 C382,210 392,280 432,335" fill="none" stroke="var(--orange)" stroke-width="4"/>
      <path d="M1020,0 L1200,0 L1200,401 L0,401 L0,60 C20,100 16,200 30,250 C45,300 80,290 140,285 C190,280 210,300 230,330 C260,360 300,355 350,340 C400,325 440,310 480,325 C530,345 560,392 640,393 C720,394 800,340 850,290 C920,210 970,90 1020,0 Z" fill="var(--sky-light)"/>
      <path d="M1122,0 L1200,0 L1200,401 L860,401 C935,335 1000,270 1040,180 C1070,110 1090,50 1122,0 Z" fill="var(--sky)"/>
      <path d="M0,338 C40,368 110,356 172,401 L0,401 Z" fill="var(--sky)"/>
    </svg>

    <svg class="layer" viewBox="0 0 1200 401" role="img" aria-label="Illustration of a head in profile with a heart and medical cross, growing from a sprout among green leaves">
      <defs>
        <linearGradient id="illustrationTone" x1="0" y1="0" x2="0" y2="1">
          <stop offset="0" stop-color="var(--head)"/>
          <stop offset="1" stop-color="var(--leaf)"/>
        </linearGradient>
      </defs>
      <path d="M870,401 C868,340 880,280 930,258 C950,200 1000,162 1060,162 C1120,162 1150,205 1150,250 C1175,262 1190,300 1192,401 Z" fill="url(#illustrationTone)"/>
    </svg>

    <div class="brand">
      <span class="brand-dot"></span>
      <span class="brand-name">PIVOT</span>
    </div>

    <h1 class="headline">
      <span class="headline-lead">Your Mental Health</span>
      <span class="headline-main">MADE SIMPLE</span>
    </h1>

    <p class="intro">PIVOT offers numerous lessons that you can apply today on your path to healing.</p>
  </div>
</body>
</html>
```